Independence Day Graphics for Sale

I want to create 10 social media graphics (new Pictora size 4:5 (1080 x 1350 pixels) focusing on our July 4th Sale Graphics, using any of the pics attached. Use the attached pics, NO RANDOM STOCK PHOTOGRAPHY. For the color scheme of the graphics, they should all be complementary to the product colors in the photos.
You can add any of the photos attached but none are required. You can do some of the graphics in all text. I mainly need BOLD text that says one of the headlines (10 total) SEE ATTACHED WORD DOCUMENT for the headlines to use.

Target Market(s)

women looking to lose weight

Requirements
Must have
• pics attached and text attached

```html
<!DOCTYPE html>
<html lang="en">
<head>
<meta charset="utf-8">
<title>July 4th Sale Graphics</title>
<link href="https://fonts.googleapis.com/css2?family=Bebas+Neue&family=Oswald:wght@400;500;700&family=Montserrat:wght@400;500&family=Tinos:wght@700&display=swap" rel="stylesheet">
<style>
:root{
  --canvas:#f4a9ab;
  --pink:#ec2a93;
  --red:#f0141c;
  --black:#111111;
  --white:#ffffff;
  --wood:#5a3426;
  --wood-dark:#2a1812;
  --counter:#e9e6e3;
  --grey-light:#eeeeee;
  --plum:#8e1255;
  --top-white:#f3efee;
  --hair:#1d1310;
}
*{margin:0;padding:0;box-sizing:border-box}
html,body{width:1200px;height:1118px;overflow:hidden;background:var(--canvas)}
.board{position:relative;width:1200px;height:1118px;font-family:'Bebas Neue',sans-serif}
.tile{position:absolute;width:241px;height:302px;overflow:hidden;background:var(--wood-dark)}
.photo{position:absolute;inset:0;background:linear-gradient(180deg,var(--wood) 0%,#3b2219 50%,#5d4c45 80%,var(--counter) 100%)}
.person{position:absolute;border-radius:55px 55px 8px 8px;background:linear-gradient(180deg,var(--hair) 0%,#3a2a24 24%,var(--top-white) 38%,#e7e2e1 60%,#b89a8a 66%,#1a1a1a 72%,#1a1a1a 100%)}
.products{position:absolute;border-radius:4px;background:linear-gradient(90deg,#f4eef1 0%,#e4ecf2 18%,#f6dfe8 34%,#e9f0ee 50%,#ecdff0 66%,#e3ebf3 82%,#f4eef1 100%)}
.abs{position:absolute;line-height:.9;color:var(--white)}
.vert{writing-mode:vertical-rl}
.up{writing-mode:vertical-rl;transform:rotate(180deg)}
.pink{color:var(--pink)}
.red{color:var(--red)}
.dark{color:var(--black)}
.thin{font-family:'Montserrat',sans-serif;font-weight:500;letter-spacing:.5px}
.tag{position:absolute;text-align:center;line-height:.9;color:var(--white)}

.t1{left:79px;top:81px}
.t2{left:352px;top:81px}
.t3{left:625px;top:81px}
.t4{left:882px;top:81px}
.t5{left:74px;top:396px}
.t6{left:348px;top:396px}
.t7{left:626px;top:396px}
.t8{left:884px;top:396px}
.t9{left:339px;top:734px}
.t10{left:617px;top:734px}

.caption{position:absolute;left:267px;top:710px;font-family:'Tinos',serif;font-weight:700;font-size:10px;color:#4a3a3a}
</style>
</head>
<body>
<div class="board">

  <!-- 1 -->
  <div class="tile t1">
    <div class="photo"></div>
    <div class="person" role="img" aria-label="Smiling woman in a white crop top pointing at the products" style="left:88px;top:32px;width:110px;height:240px"></div>
    <div class="products" role="img" aria-label="Row of supplement bottles on the counter" style="left:22px;top:224px;width:200px;height:48px"></div>
    <div class="abs" style="left:0;top:0;bottom:0;width:60px;background:linear-gradient(90deg,rgba(0,0,0,.85),rgba(0,0,0,0))"></div>
    <div class="abs" style="right:0;top:0;bottom:0;width:80px;background:linear-gradient(270deg,rgba(236,42,147,.7),rgba(236,42,147,0))"></div>
    <div class="abs" style="left:0;top:26px;width:104px;height:23px;background:var(--pink);font-size:21px;padding:2px 0 0 18px">JULY 4TH</div>
    <div class="abs vert" style="left:14px;top:60px;font-size:36px;letter-spacing:1px">MEGA <span class="pink">SALE!</span></div>
    <div class="abs" style="right:14px;top:0;width:60px;height:88px;background:var(--white);text-align:center;padding-top:16px">
      <div class="pink" style="font-size:30px;line-height:.85">25%</div>
      <div class="dark" style="font-size:30px;line-height:.85">OFF</div>
      <div class="dark" style="font-size:10px">EVERYTHING</div>
    </div>
  </div>

  <!-- 2 -->
  <div class="tile t2">
    <div class="photo"></div>
    <div class="person" role="img" aria-label="Smiling woman holding a supplement bottle" style="left:112px;top:24px;width:108px;height:278px"></div>
    <div class="products" role="img" aria-label="Two supplement bottles on the counter" style="left:130px;top:246px;width:60px;height:38px"></div>
    <div class="abs" style="left:0;top:0;bottom:0;width:130px;background:linear-gradient(90deg,rgba(0,0,0,.9),rgba(0,0,0,0))"></div>
    <div class="abs" style="right:0;top:0;bottom:0;width:90px;background:linear-gradient(270deg,rgba(236,42,147,.85),rgba(236,42,147,0))"></div>
    <div class="abs" style="left:17px;top:22px;font-size:23px">BIGGEST<br>4TH OF JULY</div>
    <div class="abs pink" style="left:14px;top:66px;font-size:56px">SALE</div>
    <div class="abs" style="left:17px;top:124px;font-size:30px">EVER!</div>
    <div class="abs" style="left:22px;top:218px;font-size:31px">25% OFF</div>
    <div class="abs thin pink" style="left:24px;top:249px;font-size:9px;letter-spacing:4px">SITEWIDE</div>
  </div>

  <!-- 3 -->
  <div class="tile t3">
    <div class="photo"></div>
    <div class="person" role="img" aria-label="Smiling woman in a white crop top pointing at the products" style="left:92px;top:22px;width:110px;height:250px"></div>
    <div class="products" role="img" aria-label="Row of supplement bottles on the counter" style="left:22px;top:222px;width:200px;height:50px"></div>
    <div class="abs" style="left:0;top:0;bottom:0;width:110px;background:linear-gradient(90deg,rgba(0,0,0,.6),rgba(0,0,0,0))"></div>
    <div class="abs" style="left:15px;top:22px;font-size:28px">HISTORIC</div>
    <div class="abs" style="left:13px;top:51px;font-size:22px">4TH OF JULY</div>
    <div class="abs pink" style="left:12px;top:74px;font-size:52px">SALE!</div>
    <div class="abs" style="left:0;right:0;top:133px;height:64px;background:rgba(236,42,147,.85);text-align:center;padding-top:7px">
      <div class="thin dark" style="font-size:34px;line-height:1">25% OFF</div>
      <div class="thin dark" style="font-size:11px;letter-spacing:3px;font-weight:400">OF EVERYTHING</div>
    </div>
  </div>

  <!-- 4 -->
  <div class="tile t4">
    <div class="photo"></div>
    <div class="person" role="img" aria-label="Smiling woman holding a supplement bottle" style="left:112px;top:24px;width:110px;height:278px"></div>
    <div class="products" role="img" aria-label="Two supplement bottles on the counter" style="left:110px;top:246px;width:50px;height:36px"></div>
    <div class="abs" style="left:0;top:0;bottom:0;width:110px;background:linear-gradient(90deg,rgba(0,0,0,.95) 40%,rgba(0,0,0,0))"></div>
    <div class="abs" style="left:17px;top:24px;font-size:32px">MEGA</div>
    <div class="abs up red" style="left:14px;top:56px;font-size:64px;line-height:.8">SUMMER</div>
    <div class="abs" style="left:17px;top:252px;font-size:25px">BLOWOUT!</div>
    <div class="tag" style="right:0;top:195px;width:90px;height:45px;background:var(--red);border-radius:6px 0 0 6px;padding-top:5px">
      <div style="font-size:28px">25% OFF</div>
      <div class="thin" style="font-size:8px;letter-spacing:2px">EVERYTHING</div>
    </div>
  </div>

  <!-- 5 -->
  <div class="tile t5">
    <div class="photo"></div>
    <div class="person" role="img" aria-label="Smiling woman holding a supplement bottle" style="left:100px;top:18px;width:112px;height:284px"></div>
    <div class="products" role="img" aria-label="Two supplement bottles on the counter" style="left:88px;top:240px;width:50px;height:36px"></div>
    <div class="abs" style="left:0;top:0;bottom:0;width:80px;background:linear-gradient(90deg,var(--black) 55%,rgba(0,0,0,0))"></div>
    <div class="abs vert" style="left:18px;top:28px;font-size:54px;line-height:.85">ONE-TIME <span class="pink">ONLY</span></div>
    <div class="tag" style="right:0;top:178px;width:120px;height:54px;background:linear-gradient(90deg,rgba(236,42,147,0),var(--pink) 25%);padding:6px 0 0 20px">
      <div style="font-size:30px">25% OFF</div>
      <div style="font-size:21px">EVERYTHING</div>
    </div>
    <svg class="abs" style="left:0;bottom:0" width="241" height="24" viewBox="0 0 241 24"><polygon points="0,6 190,24 0,24" fill="var(--pink)"/></svg>
  </div>

  <!-- 6 -->
  <div class="tile t6">
    <div class="photo"></div>
    <div class="person" role="img" aria-label="Smiling woman holding a supplement bottle" style="left:40px;top:80px;width:130px;height:222px"></div>
    <div class="abs" style="left:0;right:0;top:0;height:90px;background:linear-gradient(180deg,rgba(0,0,0,.6),rgba(0,0,0,0))"></div>
    <div class="abs" style="left:30px;top:12px;font-size:58px"><span class="red">25%</span> OFF</div>
    <div class="abs" style="left:32px;top:66px;font-family:'Oswald',sans-serif;font-weight:500;font-size:11px">STOCK-UP EVENT &amp; <span class="red">ALL SUPPLEMENTS</span></div>
    <svg class="abs" style="left:60px;top:155px" width="180" height="125" viewBox="0 0 180 125">
      <g transform="rotate(12 90 60)">
        <rect x="15" y="20" width="150" height="85" fill="var(--white)" stroke="var(--red)" stroke-width="3"/>
      </g>
      <rect x="12" y="20" width="148" height="90" fill="var(--grey-light)" stroke="var(--red)" stroke-width="3"/>
    </svg>
    <div class="products" role="img" aria-label="Row of four supplement bottles" style="left:80px;top:190px;width:130px;height:64px"></div>
    <svg class="abs" style="left:0;bottom:0" width="241" height="25" viewBox="0 0 241 25"><polygon points="0,8 241,18 241,25 0,25" fill="var(--red)"/><polygon points="0,5 241,14 241,18 0,9" fill="var(--black)"/></svg>
  </div>

  <!-- 7 -->
  <div class="tile t7" style="background:var(--grey-light)">
    <div class="abs" style="inset:0;background:linear-gradient(180deg,#ffffff,#e2e2e2)"></div>
    <div class="abs dark" style="left:18px;top:18px;font-size:22px">THE LOWEST</div>
    <div class="abs red" style="left:17px;top:38px;font-size:46px">PRICES</div>
    <div class="abs dark" style="left:19px;top:82px;font-size:22px">WE'VE EVER</div>
    <div class="abs dark" style="left:17px;top:102px;font-size:48px">OFFERED!</div>
    <div class="tag" style="right:20px;top:0;width:44px;height:148px;background:linear-gradient(180deg,var(--red) 70%,rgba(240,20,28,0))">
      <div class="vert" style="font-size:38px;margin:10px auto 0;line-height:1">25% OFF</div>
    </div>
    <div class="products" role="img" aria-label="Four large supplement bottles on a white surface" style="left:18px;top:160px;width:212px;height:102px;border-radius:8px"></div>
    <svg class="abs" style="left:0;bottom:0" width="241" height="55" viewBox="0 0 241 55"><polygon points="0,20 241,46 241,55 0,55" fill="var(--plum)"/><polygon points="0,20 120,32 0,36" fill="var(--pink)"/></svg>
  </div>

  <!-- 8 -->
  <div class="tile t8">
    <div class="photo"></div>
    <div class="person" role="img" aria-label="Smiling woman holding a supplement bottle" style="left:110px;top:22px;width:110px;height:280px"></div>
    <div class="products" role="img" aria-label="Two supplement bottles on the counter" style="left:104px;top:240px;width:50px;height:36px"></div>
    <div class="abs" style="left:0;top:0;bottom:0;width:110px;background:linear-gradient(90deg,rgba(0,0,0,.9) 40%,rgba(0,0,0,0))"></div>
    <div class="abs" style="left:21px;top:28px;font-size:25px">OUR BIGGEST</div>
    <div class="abs up red" style="left:16px;top:50px;font-size:62px;line-height:.8">DISCOUNT</div>
    <div class="abs" style="left:17px;top:246px;font-size:30px">EVER!</div>
    <div class="tag" style="right:0;top:175px;width:120px;height:58px;background:linear-gradient(90deg,rgba(240,20,28,0),var(--red) 20%);padding:6px 0 0 18px">
      <div style="font-size:32px">25% OFF</div>
      <div style="font-size:22px">EVERYTHING</div>
    </div>
    <svg class="abs" style="left:0;bottom:0" width="241" height="24" viewBox="0 0 241 24"><polygon points="0,8 200,24 0,24" fill="var(--pink)"/></svg>
  </div>

  <!-- 9 -->
  <div class="tile t9">
    <div class="photo"></div>
    <div class="person" role="img" aria-label="Smiling woman in a white crop top pointing at the products" style="left:66px;top:20px;width:110px;height:250px"></div>
    <div class="products" role="img" aria-label="Row of supplement bottles on the counter" style="left:18px;top:220px;width:206px;height:52px"></div>
    <div class="abs" style="left:16px;top:26px;font-size:48px;transform:skewY(8deg) scaleY(1.35);transform-origin:top left">DON'T</div>
    <div class="abs" style="left:160px;top:26px;font-size:52px;transform:skewY(-10deg) scaleY(1.35);transform-origin:top left">WAIT</div>
    <div class="abs" style="left:0;right:0;top:127px;height:64px;background:rgba(240,40,50,.85);text-align:center;padding-top:8px">
      <div class="thin" style="font-size:34px;line-height:1">25% OFF</div>
      <div class="thin" style="font-size:13px;letter-spacing:3px;font-weight:400">END SOON</div>
    </div>
  </div>

  <!-- 10 -->
  <div class="tile t10">
    <div class="photo"></div>
    <div class="person" role="img" aria-label="Smiling woman in a white crop top pointing at the products" style="left:66px;top:20px;width:110px;height:250px"></div>
    <div class="products" role="img" aria-label="Row of supplement bottles on the counter" style="left:18px;top:222px;width:206px;height:50px"></div>
    <div class="abs pink" style="left:18px;top:22px;font-size:32px">LAST</div>
    <div class="abs vert" style="left:18px;top:54px;font-size:40px;line-height:.85">CHANCE</div>
    <div class="tag" style="right:22px;top:0;width:34px;height:130px;background:var(--pink)">
      <div class="vert" style="font-size:30px;margin:10px auto 0;line-height:1.1">25% OFF</div>
    </div>
    <svg class="abs" style="left:0;top:135px" width="241" height="80" viewBox="0 0 241 80">
      <path d="M0,40 Q60,22 120,20 T241,4 L241,44 Q180,50 120,58 T0,80 Z" fill="var(--white)"/>
      <path d="M0,44 Q60,26 120,24 T241,8 L241,40 Q180,46 120,54 T0,76 Z" fill="var(--pink)"/>
    </svg>
    <div class="abs" style="left:34px;top:168px;font-family:'Oswald',sans-serif;font-weight:700;font-size:21px;transform:rotate(-7deg);white-space:nowrap">TIME IS RUNNING OUT!</div>
  </div>

  <div class="caption">1.25% OFF Stock-Up Event:&nbsp; 25% OFF All Supplements</div>

</div>
</body>
</html>
```